Norvale Investment Management Needs Door Wording Design

We need someone to put together a design for our glass front doors (2).

The words could be, but aren't limited to, as follows:

"100
Gently Restored Bodywork Studio
*Ring Bell"

and

"200 & 300
Norvale Investment Management inc.
*Ring Bell"

The design should be clean, subtle and professional. It is a simple mainly glass door with a black frame. Our website is www.norvaleinvest.ca for a more detailed description of what we do. The adjacent business would also be involved, as per the wording of the Gently Restored Bodywork Studio.

We are looking for something to bring out the wording on the door (there is currently a piece of paper printed and taped to the inside).

Dimensions of the window are 47 inches x 23 inches.

Thanks!

Colors
000000
ffffff

Requirements
Must have
• The previous words
Nice to have
• Creative flair, taking into consideration the nature of our business (Investment Management)

```html
<!DOCTYPE html>
<html lang="en">
<head>
<meta charset="utf-8">
<title>Norvale Project – Door Lettering</title>
<link rel="stylesheet" href="https://fonts.googleapis.com/css2?family=Bebas+Neue&family=Roboto:wght@300&display=swap">
<style>
  :root {
    --ink: #000000;
    --paper: #ffffff;
  }
  html, body {
    margin: 0;
    padding: 0;
    background: var(--paper);
    overflow: hidden;
  }
  .sheet {
    display: block;
    width: 927px;
    height: 1200px;
  }
  .title-block__frame,
  .door-panel__outline {
    fill: none;
    stroke: var(--ink);
    stroke-width: 1.6;
  }
  .title-block__text {
    font-family: "Roboto", Arial, sans-serif;
    font-weight: 300;
    font-size: 30px;
    fill: var(--ink);
  }
  .door-lettering {
    font-family: "Bebas Neue", "Arial Narrow", sans-serif;
    fill: var(--ink);
  }
  .bracket {
    fill: none;
    stroke: var(--ink);
    stroke-width: 12;
    stroke-linecap: butt;
    stroke-linejoin: round;
  }
</style>
</head>
<body>
<svg class="sheet" viewBox="0 0 927 1200" xmlns="http://www.w3.org/2000/svg">
  <rect width="927" height="1200" fill="var(--paper)"/>

  <!-- Title block -->
  <g class="title-block">
    <rect class="title-block__frame" x="126" y="24" width="772" height="76"/>
    <text class="title-block__text" x="888" y="55" text-anchor="end">NORVALE PROJECT</text>
    <text class="title-block__text" x="888" y="90" text-anchor="end">MARCH 13, 2017</text>
  </g>

  <!-- Door 100: bodywork studio -->
  <g class="door-panel door-panel--studio">
    <rect class="door-panel__outline" x="62" y="245" width="338" height="691"/>
    <text class="door-lettering suite-number" x="82" y="332" font-size="90" textLength="124" lengthAdjust="spacingAndGlyphs">100</text>
    <path class="bracket" d="M214 278 H364 A8 8 0 0 1 372 286 V472"/>
    <path class="bracket" d="M90 346 V472"/>
    <text class="door-lettering business-name" x="82" y="522" font-size="46" textLength="300" lengthAdjust="spacingAndGlyphs">GENTLY RESTORED</text>
    <text class="door-lettering business-name" x="82" y="592" font-size="83" textLength="298" lengthAdjust="spacingAndGlyphs">BODYWORK</text>
    <text class="door-lettering business-name" x="82" y="676" font-size="94" textLength="300" lengthAdjust="spacingAndGlyphs">STUDIO</text>
    <path class="bracket" d="M90 692 V894 A8 8 0 0 0 98 902 H222"/>
    <path class="bracket" d="M372 692 V760"/>
    <text class="door-lettering call-to-action" x="252" y="822" font-size="60" textLength="124" lengthAdjust="spacingAndGlyphs">RELAX</text>
    <text class="door-lettering call-to-action" x="252" y="882" font-size="71" textLength="122" lengthAdjust="spacingAndGlyphs">NOW</text>
    <text class="door-lettering bell-note" x="252" y="906" font-size="17" textLength="126" lengthAdjust="spacingAndGlyphs">JUST RING THE BELL</text>
  </g>

  <!-- Doors 200 & 300: investment management -->
  <g class="door-panel door-panel--investment">
    <rect class="door-panel__outline" x="526" y="244" width="339" height="691"/>
    <text class="door-lettering suite-number" x="550" y="332" font-size="80" textLength="126" lengthAdjust="spacingAndGlyphs">300</text>
    <text class="door-lettering suite-number" x="550" y="404" font-size="83" textLength="126" lengthAdjust="spacingAndGlyphs">200</text>
    <path class="bracket" d="M684 276 H833 A8 8 0 0 1 841 284 V452"/>
    <path class="bracket" d="M556 422 V450"/>
    <text class="door-lettering business-name" x="550" y="574" font-size="154" textLength="298" lengthAdjust="spacingAndGlyphs">NORVALE</text>
    <text class="door-lettering business-name" x="550" y="662" font-size="69" textLength="296" lengthAdjust="spacingAndGlyphs">INVESTMENT</text>
    <text class="door-lettering business-name" x="550" y="708" font-size="49" textLength="304" lengthAdjust="spacingAndGlyphs">MANAGEMENT INC.</text>
    <path class="bracket" d="M556 720 V891 A8 8 0 0 0 564 899 H688"/>
    <path class="bracket" d="M841 720 V758"/>
    <text class="door-lettering call-to-action" x="716" y="816" font-size="63" textLength="126" lengthAdjust="spacingAndGlyphs">INVEST</text>
    <text class="door-lettering call-to-action" x="716" y="880" font-size="74" textLength="122" lengthAdjust="spacingAndGlyphs">NOW</text>
    <text class="door-lettering bell-note" x="716" y="902" font-size="17" textLength="126" lengthAdjust="spacingAndGlyphs">JUST RING THE BELL</text>
  </g>
</svg>
</body>
</html>
```